Business card for real estate agent / office

We're looking for a new business card. We want something that is pretty clean, modern and sleek. Something that also tells people that we are a new age company...cutting edge. Although real estate has been done a certain way the last 100 years, we have energy and vibrance. Company name is Silver Meadow Properties. info can be found here: http://www.smprealtyhub.example/

needs to include: Name, title, phone number, email. our license number also needs to be displayed somewhere.

Target Market(s)

25-55 homeowners or potential homeowners

Industry/Entity Type

Business

Contact Information for Business Card

we need business card designs for real estate agent / office

Font styles to use
Serif

Requirements
Must have
• needs to include: Name, title, phone number, email. our license number also needs to be displayed somewhere and company name.
Nice to have
• placement area for photo

```html
<!DOCTYPE html>
<html lang="en">
<head>
<meta charset="utf-8">
<title>Silver Meadow Properties – Business Card</title>
<link href="https://fonts.googleapis.com/css2?family=Nunito+Sans:wght@400;600;700&display=swap" rel="stylesheet">
<style>
  :root {
    --backdrop: #e6e7e9;
    --navy: #073a61;
    --navy-deep: #052c4b;
    --green: #5bb944;
    --green-deep: #47a332;
    --white: #ffffff;
    --ink: #10365a;
  }
  * { margin: 0; padding: 0; box-sizing: border-box; }
  html, body {
    width: 1200px;
    height: 1200px;
    overflow: hidden;
  }
  body {
    background: var(--backdrop);
    font-family: "Nunito Sans", "Helvetica Neue", Arial, sans-serif;
    position: relative;
  }
  .card {
    position: absolute;
    left: 210px;
    width: 780px;
    height: 444px;
    box-shadow: 0 6px 18px rgba(0, 0, 0, 0.25);
    overflow: hidden;
  }
  .card-front {
    top: 110px;
    background: radial-gradient(ellipse at 50% 40%, var(--navy) 0%, var(--navy) 45%, var(--navy-deep) 100%);
    display: flex;
    align-items: center;
    justify-content: center;
  }
  .brand-name {
    color: var(--white);
    font-weight: 700;
    font-size: 40px;
    letter-spacing: 0.2px;
  }
  .card-back {
    top: 646px;
    background: var(--white);
  }
  .house-shape {
    position: absolute;
    inset: 0;
    width: 100%;
    height: 100%;
  }
  .agent {
    position: absolute;
    right: 32px;
    top: 38px;
    text-align: right;
  }
  .agent-name {
    color: var(--green);
    font-weight: 700;
    font-size: 42px;
    line-height: 1.1;
  }
  .agent-title {
    margin-top: 22px;
    color: var(--green);
    font-size: 22px;
    line-height: 1.35;
  }
  .contact {
    position: absolute;
    right: 32px;
    bottom: 34px;
    text-align: right;
    color: var(--ink);
    font-size: 21px;
    line-height: 1.35;
  }
  .license {
    position: absolute;
    left: 31px;
    bottom: 34px;
    color: var(--white);
    font-size: 20px;
  }
</style>
</head>
<body>
  <section class="card card-front">
    <div class="brand-name">Silver Meadow Properties</div>
  </section>

  <section class="card card-back">
    <svg class="house-shape" viewBox="0 0 780 444" preserveAspectRatio="none" aria-hidden="true">
      <defs>
        <linearGradient id="house-fill" x1="0" y1="0" x2="1" y2="1">
          <stop offset="0" stop-color="#5bb944"/>
          <stop offset="1" stop-color="#4fae39"/>
        </linearGradient>
      </defs>
      <polygon points="0,0 228,0 392,184 307,184 307,444 0,444" fill="url(#house-fill)"/>
    </svg>

    <div class="agent">
      <div class="agent-name">Daniel Moreno</div>
      <div class="agent-title">Real Estate Broker,<br>Realtor, MBA</div>
    </div>

    <div class="contact">
      <div>m: 310.555.0148</div>
      <div>e: dan@silvermeadowprop.example</div>
      <div>w: silvermeadow.example</div>
    </div>

    <div class="license">CA BRE #02917358</div>
  </section>
</body>
</html>
```